Online business manager needs a website

I need a website designed and then coded. I am an online business manager serving a number of different industries providing administrative support to existing small businesses and helping solo practitioners get their new business up and running.

I didn't have a logo formally designed but have been using the attached avatar and wouldn't mind something that incorporated that.

The business doesn't have an official name, so I've just been using my name Lena Pruvost, Online Business Manager or Lena Pruvost, OBM. I've attached two documents that I have made previously for an example of content.

I would prefer the final site be in Wordpress.

Requirements
Must have
• A way to contact me, testimonials, list of services

```html
<!DOCTYPE html>
<html lang="en">
<head>
<meta charset="UTF-8">
<title>Lena Pruvost — Online Business Manager</title>
<link rel="stylesheet" href="https://fonts.googleapis.com/css2?family=Pacifico&family=Poppins:wght@400;500;600&display=swap">
<style>
:root{
  --purple-deep:#4a1a9a;
  --purple-mid:#6a1a8a;
  --violet:#5a2a9c;
  --lavender:#f1eafc;
  --ink:#1a1a1a;
  --text:#333;
  --gray-bg:#f3f3f5;
  --star:#f08a1c;
  --white:#fff;
}
*{box-sizing:border-box;margin:0;padding:0}
html,body{width:1200px;height:3351px;overflow:hidden}
body{font-family:"Poppins",sans-serif;color:var(--text);background:var(--white);position:relative}
section,header,footer{position:absolute;left:0;width:1200px}

.site-header{top:0;height:88px;background:var(--white)}
.brand{position:absolute;left:104px;top:14px}
.brand-name{font-family:"Pacifico",cursive;color:var(--purple-mid);font-size:24px;line-height:34px}
.brand-tag{font-size:12px;color:var(--ink);margin-top:-2px}
.menu-toggle{position:absolute;left:1073px;top:38px;width:22px}
.menu-toggle span{display:block;height:3px;background:var(--ink);margin-bottom:5px;border-radius:2px}

.hero{top:88px;height:530px;background:linear-gradient(100deg,#7a1481 0%,#6a1a8a 45%,#4a1d9c 100%)}
.hero-text{position:absolute;left:104px;top:110px;width:470px;color:var(--white)}
.hero-text h1{font-family:"Pacifico",cursive;font-size:44px;line-height:56px;font-weight:400}
.hero-text h2{font-family:"Pacifico",cursive;font-size:30px;line-height:44px;font-weight:400}
.hero-role{font-size:15px;margin:4px 0 14px}
.lead{font-size:14.5px;line-height:28px}
.btn-outline{display:inline-block;margin-top:24px;border:2px solid var(--white);border-radius:22px;padding:6px 20px;color:var(--white);font-family:"Pacifico",cursive;font-size:14px}
.hero-photo{position:absolute;left:659px;top:57px;width:426px;height:487px;border-radius:6px;background:linear-gradient(160deg,#c0407a 0%,#8a2d5a 40%,#2a2a33 100%);z-index:2}

.services{top:618px;height:539px}
.services h2{position:absolute;left:104px;top:60px;font-family:"Pacifico",cursive;font-size:40px;font-weight:400;color:var(--ink)}
.services-intro{position:absolute;left:600px;top:72px;width:500px;font-size:14px;line-height:28px}
.service-card{position:absolute;top:185px;width:226px;height:272px;background:var(--white);box-shadow:0 2px 12px rgba(0,0,0,.12);border-radius:4px;overflow:hidden;text-align:center}
.service-img{height:193px;background:linear-gradient(160deg,#0c2f7a,#061a48)}
.service-card h3{font-weight:500;font-size:16.5px;color:var(--ink);height:79px;display:flex;align-items:center;justify-content:center;line-height:26px}

.rates{top:1157px;height:570px;background:linear-gradient(180deg,#5a2a9a 0%,#5326a0 60%,#4c22a6 100%)}
.rates h2{position:absolute;left:0;width:1200px;top:65px;text-align:center;color:var(--white);font-family:"Pacifico",cursive;font-size:42px;font-weight:400}
.rate-card{position:absolute;top:181px;width:257px;height:268px;background:var(--white);border-radius:16px;overflow:hidden;text-align:center}
.rate-head{background:var(--lavender);height:90px;padding-top:22px;color:var(--violet);font-weight:600;font-size:18px;line-height:26px}
.rate-list{list-style:none;margin-top:18px;font-size:13.5px;line-height:30px}
.rate-list li{color:var(--ink)}
.rate-list li::before{content:"";display:inline-block;width:8px;height:8px;border-radius:50%;background:var(--ink);margin-right:3px;vertical-align:1px}
.btn-pill{display:inline-block;margin-top:8px;background:var(--purple-mid);color:var(--white);border-radius:18px;padding:3px 18px;font-family:"Pacifico",cursive;font-size:13px}
.rate-note{font-size:12.5px;color:#444;margin-top:6px}

.testimonials{top:1727px;height:535px}
.client-photo{position:absolute;left:140px;top:83px;width:370px;height:370px;border-radius:50%;background:radial-gradient(circle at 50% 40%,#a0b070 0%,#6a7a40 60%,#4a5230 100%)}
.testimonials h2{position:absolute;left:639px;top:120px;font-family:"Pacifico",cursive;font-size:40px;font-weight:400;color:var(--ink)}
.quote{position:absolute;left:639px;top:183px;width:465px;font-size:14.5px;line-height:29px;color:var(--ink)}
.stars{position:absolute;left:639px;top:345px;color:var(--star);font-size:15px;letter-spacing:5px}
.client-name{position:absolute;left:639px;top:378px;font-family:"Pacifico",cursive;color:var(--purple-deep);font-size:16px}

.work{top:2262px;height:534px;background:var(--gray-bg);overflow:hidden}
.work-deco{position:absolute;left:270px;top:40px;width:140px;height:140px;border-radius:50%;background:#fafafa}
.work h2{position:absolute;left:104px;top:110px;font-family:"Pacifico",cursive;font-size:40px;line-height:54px;font-weight:400;color:var(--ink)}
.work p{position:absolute;left:104px;top:236px;width:390px;font-size:14.5px;line-height:26.5px;color:var(--ink)}
.work-arrow{position:absolute;left:104px;top:383px}
.work-thumb{position:absolute;width:224px;height:185px;border:4px solid var(--white)}

.contact{top:2796px;height:467px;background:linear-gradient(100deg,#5a1078 0%,#7a1482 50%,#8a1a7a 100%);overflow:hidden}
.contact-deco{position:absolute;left:0;top:0}
.contact-art{position:absolute;left:130px;top:60px;width:467px;height:395px;border-radius:6px;background:linear-gradient(180deg,#f0d070 0%,#2e8a6a 55%,#9a9aa0 100%)}
.contact h2{position:absolute;left:654px;top:52px;font-family:"Pacifico",cursive;font-size:40px;font-weight:400;color:var(--white)}
.contact-list{position:absolute;left:652px;top:126px;list-style:none;color:var(--white);font-weight:600;font-size:21px}
.contact-list li{display:flex;align-items:center;height:58px}
.contact-list svg{margin-right:12px}

.site-footer{top:3263px;height:88px;text-align:center;font-size:12px;color:#333;padding-top:52px}
</style>
</head>
<body>

<header class="site-header">
  <div class="brand">
    <div class="brand-name">Lena Pruvost</div>
    <div class="brand-tag">Online Business Manager</div>
  </div>
  <div class="menu-toggle" aria-label="Menu"><span></span><span></span><span></span></div>
</header>

<section class="hero">
  <div class="hero-text">
    <h1>About Me</h1>
    <h2>Lena Pruvost</h2>
    <div class="hero-role">Online Business Manager</div>
    <p class="lead">Hi! I'm so excited that you have chosen to explore my portfolio. Helping businesses achieve their goals is my passion, and I'm thrilled that with my assistance you will have more time for your own passion project. I thrive while working independently, which means you can be confident when leaving tasks for me.</p>
    <span class="btn-outline">Read More</span>
  </div>
  <div class="hero-photo" role="img" aria-label="Portrait photo of Lena in front of pink flowering bushes"></div>
</section>

<section class="services">
  <h2>About Services</h2>
  <p class="services-intro">Lorem ipsum dolor sit amet, consectetur adipiscing elit, sed do eiusmod tempor incididunt ut labore et dolore magna aliqua. Quis ipsum suspendisse ultrices gravida.</p>
  <div class="service-card" style="left:104px"><div class="service-img" role="img" aria-label="Photo of hands typing with a cloud interface overlay"></div><h3>Virtual Assistance</h3></div>
  <div class="service-card" style="left:360px"><div class="service-img" role="img" aria-label="Photo of a phone with floating social media reactions" style="background:linear-gradient(160deg,#4a3a3a,#1a1414)"></div><h3>Social Media &amp;<br>Content Management</h3></div>
  <div class="service-card" style="left:615px"><div class="service-img" role="img" aria-label="Photo of a hand holding a glowing percentage finance graphic" style="background:linear-gradient(160deg,#1a2a4a,#0a1428)"></div><h3>Finance Management</h3></div>
  <div class="service-card" style="left:871px"><div class="service-img" role="img" aria-label="Photo of hands holding a business network graphic" style="background:linear-gradient(160deg,#2a4a5a,#102430)"></div><h3>Business Management</h3></div>
</section>

<section class="rates">
  <h2>Rates And Packages</h2>
  <div class="rate-card" style="left:57px">
    <div class="rate-head">$40<br>Hourly Rate</div>
    <ul class="rate-list"><li>For clients</li><li>Needing only</li><li>Occasional help</li></ul>
    <span class="btn-pill">Read More</span>
  </div>
  <div class="rate-card" style="left:334px">
    <div class="rate-head">$70<br>20 hours/month</div>
    <ul class="rate-list"><li>Includes one</li><li>15 minute meeting</li><li>Per week</li></ul>
    <span class="btn-pill">Read More</span>
    <div class="rate-note">Responses within 72 hours</div>
  </div>
  <div class="rate-card" style="left:610px">
    <div class="rate-head">$1,300<br>40 hours/month</div>
    <ul class="rate-list"><li>Includes one 30</li><li>Minute meeting</li><li>Per week</li></ul>
    <span class="btn-pill">Read More</span>
    <div class="rate-note">Responses within 48 hours</div>
  </div>
  <div class="rate-card" style="left:886px">
    <div class="rate-head">$2400<br>80 hours/month</div>
    <ul class="rate-list"><li>Includes one 40</li><li>Minute meeting</li><li>Per week</li></ul>
    <span class="btn-pill">Read More</span>
    <div class="rate-note">Responses within 24 hours</div>
  </div>
</section>

<section class="testimonials">
  <div class="client-photo" role="img" aria-label="Circular portrait photo of the client outdoors"></div>
  <h2>Client Testimonials</h2>
  <p class="quote">When it became apparent that a project would take more time than I had, Lena stepped up to take on the required research. She was thorough and timely; able to meet a last-minute 12-hour deadline. I would highly recommend Lena to assist with your next project.</p>
  <div class="stars">★★★★★</div>
  <div class="client-name">Dana R. Owner, Summit Ridge Exteriors</div>
</section>

<section class="work">
  <div class="work-deco"></div>
  <h2>About<br>Our Work</h2>
  <p>focused on the live event and entertainment industry. Helping artists and owners to better manage their career and business by strategically reviewing systems, recommending operational efficiencies, and managing inboxes</p>
  <svg class="work-arrow" width="50" height="22" viewBox="0 0 50 22"><path d="M0 11H48M38 2l10 9-10 9" fill="none" stroke="#1a1a1a" stroke-width="2"/></svg>
  <div class="work-thumb" style="left:634px;top:56px;background:linear-gradient(135deg,#fbeee6,#f3d8c6)" role="img" aria-label="Podcast promo graphic about business workflows and automations"></div>
  <div class="work-thumb" style="left:874px;top:56px;background:#f4595a" role="img" aria-label="Red quote graphic about skipping full glam"></div>
  <div class="work-thumb" style="left:634px;top:260px;background:linear-gradient(135deg,#f7f3f0,#e8e0da)" role="img" aria-label="Podcast episode graphic about mindful body movement"></div>
  <div class="work-thumb" style="left:874px;top:260px;background:#f98a3c" role="img" aria-label="Orange graphic with five tips for looking great on video calls"></div>
</section>

<section class="contact">
  <svg class="contact-deco" width="1200" height="467" viewBox="0 0 1200 467"><path d="M0 380L90 290L260 467" fill="none" stroke="rgba(255,255,255,.35)" stroke-width="2"/><path d="M620 467L1200 130" fill="none" stroke="rgba(255,255,255,.12)" stroke-width="2"/></svg>
  <div class="contact-art" role="img" aria-label="Cartoon avatar waving from a laptop screen"></div>
  <h2>Contact Me</h2>
  <ul class="contact-list">
    <li><svg width="26" height="26" viewBox="0 0 24 24"><path d="M6.6 10.8a15 15 0 006.6 6.6l2.2-2.2c.3-.3.7-.4 1-.2 1.1.4 2.3.6 3.6.6.6 0 1 .4 1 1V20c0 .6-.4 1-1 1A17 17 0 013 4c0-.6.4-1 1-1h3.5c.6 0 1 .4 1 1 0 1.2.2 2.4.6 3.6.1.3 0 .7-.2 1z" fill="none" stroke="#fff" stroke-width="1.6"/></svg>555.214.0917</li>
    <li><svg width="26" height="20" viewBox="0 0 26 20"><rect x="1" y="1" width="24" height="18" fill="#fff"/><path d="M1 1l12 10L25 1" fill="none" stroke="#7a1482" stroke-width="2"/></svg>lena.pruvost@examplemail.com</li>
    <li><svg width="26" height="26" viewBox="0 0 26 26"><circle cx="13" cy="13" r="11.5" fill="none" stroke="#fff" stroke-width="1.6"/></svg>Lena Marie Pruvost</li>
    <li><svg width="26" height="26" viewBox="0 0 26 26"><circle cx="13" cy="13" r="11.5" fill="none" stroke="#fff" stroke-width="1.6"/></svg>LenaPru07</li>
  </ul>
</section>

<footer class="site-footer">Copyright © 2023 Lena Pruvost, OBM | All Rights Reserved</footer>

</body>
</html>
```